Crestbacking Banner Ad Campaign

Overview
We require 3 different banners within the same brief, but would like you to just produce 1 banner for your initial bid.

We require a punchy message to be delivered to existing poker players. We offer the opportunity for players to play poker with our money (ie. ‘staked’), sharing the profits if they win, us taking the losses if they lose. 'Sharks' is a poker term for skilled winning players who eat up the 'fish'.. term for unskilled losing players.

The players we stake are playing no risk poker and enjoy the support of our team, as well as professional coaching free of charge. Our key messages are bulleted below, some suggestions for tag lines also. We would like some creativity input in the design/ tag lines plus of course the banners themselves delivered. See www.crestbacking-example.com for our colour scheme and shark fin logo and to get a feel for what we do.

3 different pieces of artwork required:-
2 'square', sized – 180x150
1 'normal' banner sized
Clearly we may want to resize these slightly for different uses.

Some messages we want to convey:-
• Free Bankroll $$$$
• Free Pro Coaching
• Part of a team & support network
• Risk free, stress free poker
• We are the best staking operation

Possible tag lines:-
Losing your bite?
Sharpen your teeth!
Get staked today!
Join the best, crush the rest

Thanks
Alan
Updates

Guys,

we have a strong theme with the Shark and/or our red fin logo, can you focus on that in your designs please. a Shark as per brief is a successful poker player .. a 'fish' is what they prey on..

Thanks

Alan

Industry/Entity Type

Campaign

```html
<!DOCTYPE html>
<html lang="en">
<head>
<meta charset="utf-8">
<title>Crestbacking Banner – Lost Your Bite?</title>
<link rel="stylesheet" href="https://fonts.googleapis.com/css2?family=Noto+Sans:wght@700;800&display=swap">
<style>
  :root {
    --ink-black: #000000;
    --shark-red: #ff0a1e;
    --deep-red: #b0000f;
    --silver-top: #ffffff;
    --silver-bottom: #8a8a8a;
    --gold-top: #fff36a;
    --gold-bottom: #f2c400;
    --bullet-white: #ffffff;
    --shark-brown: #b8361e;
    --shark-dark: #6e1a0c;
  }
  html, body {
    margin: 0;
    padding: 0;
    overflow: hidden;
    background: var(--ink-black);
  }
  .banner {
    position: relative;
    width: 1200px;
    height: 1000px;
    overflow: hidden;
    background: var(--ink-black);
    font-family: "Noto Sans", Verdana, sans-serif;
    font-weight: 700;
  }
  .banner__panel {
    position: absolute;
    left: 0;
    top: 268px;
    width: 1200px;
    height: 732px;
    background: linear-gradient(to bottom,
      var(--shark-red) 0%,
      var(--shark-red) 62%,
      var(--deep-red) 82%,
      var(--ink-black) 100%);
  }
  .headline {
    position: absolute;
    left: 0;
    top: 38px;
    width: 1200px;
    margin: 0;
    text-align: center;
    font-size: 100px;
    line-height: 1;
    letter-spacing: 1px;
    color: var(--silver-top);
    background: linear-gradient(to bottom, var(--silver-top) 35%, var(--silver-bottom) 100%);
    -webkit-background-clip: text;
    background-clip: text;
    -webkit-text-fill-color: transparent;
  }
  .call-to-action {
    position: absolute;
    left: 320px;
    top: 285px;
    margin: 0;
    font-size: 92px;
    line-height: 1;
    letter-spacing: 1px;
    background: linear-gradient(to bottom, var(--gold-top) 40%, var(--gold-bottom) 100%);
    -webkit-background-clip: text;
    background-clip: text;
    -webkit-text-fill-color: transparent;
  }
  .benefits {
    position: absolute;
    left: 110px;
    top: 420px;
    margin: 0;
    padding: 0;
    list-style: none;
  }
  .benefits__item {
    display: flex;
    align-items: center;
    height: 82px;
    font-size: 57px;
    color: var(--bullet-white);
    white-space: nowrap;
  }
  .benefits__marker {
    width: 30px;
    height: 30px;
    margin: 0 86px 0 20px;
    border-radius: 50%;
    background: var(--ink-black);
    flex: none;
  }
  .shark-illustration {
    position: absolute;
    left: 880px;
    top: 128px;
    width: 300px;
    height: 380px;
    border-radius: 46% 40% 30% 30% / 38% 34% 22% 22%;
    background: radial-gradient(ellipse at 40% 50%, var(--shark-brown) 0%, var(--shark-dark) 100%);
  }
  .tagline {
    position: absolute;
    left: 0;
    top: 795px;
    width: 1200px;
    margin: 0;
    text-align: center;
    font-size: 108px;
    line-height: 1;
    letter-spacing: 1px;
  }
  .tagline__lead {
    background: linear-gradient(to bottom, var(--silver-top) 35%, var(--silver-bottom) 100%);
    -webkit-background-clip: text;
    background-clip: text;
    -webkit-text-fill-color: transparent;
  }
  .tagline__accent {
    background: linear-gradient(to bottom, var(--shark-dark) 0%, var(--ink-black) 70%);
    -webkit-background-clip: text;
    background-clip: text;
    -webkit-text-fill-color: transparent;
  }
</style>
</head>
<body>
  <main class="banner">
    <div class="banner__panel"></div>

    <h1 class="headline">LOST YOUR BITE?</h1>

    <div class="shark-illustration" role="img" aria-label="Illustration of a red shark head with open jaws full of teeth"></div>

    <p class="call-to-action">JOIN NOW</p>

    <ul class="benefits">
      <li class="benefits__item"><span class="benefits__marker"></span>Free Bank Roll $$</li>
      <li class="benefits__item"><span class="benefits__marker"></span>Free Pro Coaching</li>
      <li class="benefits__item"><span class="benefits__marker"></span>Risk Free, Stress Free Poker</li>
      <li class="benefits__item"><span class="benefits__marker"></span>Best Staking Operation</li>
    </ul>

    <p class="tagline"><span class="tagline__lead">BECOME A </span><span class="tagline__accent">SHARK!</span></p>
  </main>
</body>
</html>
```